Business Card Design Project

Tarvolink - based in Melbourne, Australia. We plan, design, implement and support network infrastructure (Plemba, Hollvask, Q8, Stormpike etc).

Target Market(s)

Small/Medium enterprise and Corporate.

Industry/Entity Type

Business

```html
<!DOCTYPE html>
<html lang="en">
<head>
<meta charset="utf-8">
<title>Tarvolink business card</title>
<link rel="stylesheet" href="https://fonts.googleapis.com/css2?family=Questrial&display=swap">
<style>
  :root {
    --bg: #ecebe8;
    --card-black: #0b0b0b;
    --mark-faint: #1f1f1f;
    --ring-faint: #2e2823;
    --orange: #c8741e;
    --front-text: #c9c9c9;
    --card-light-top: #ffffff;
    --card-light-bottom: #c9c9c9;
    --band-dark: #5b5b5b;
    --band-name: #6c6c6c;
    --name-ink: #2f2f2f;
    --contact-ink: #4d4d4d;
    --white: #ffffff;
  }
  * { margin: 0; padding: 0; box-sizing: border-box; }
  html, body { width: 1200px; height: 900px; overflow: hidden; }
  body {
    background: var(--bg);
    font-family: "Questrial", "Century Gothic", sans-serif;
    position: relative;
  }
  .card {
    position: absolute;
    width: 560px;
    height: 320px;
    border-radius: 18px;
    overflow: hidden;
    box-shadow: 0 10px 28px rgba(0,0,0,0.25);
  }

  /* Front */
  .card-front { left: 80px; top: 110px; background: var(--card-black); }
  .front-decoration { position: absolute; right: -40px; top: 20px; }
  .front-brand {
    position: absolute; left: 60px; bottom: 70px;
    display: flex; align-items: center; gap: 10px;
  }
  .brand-dot { width: 34px; height: 34px; border-radius: 50%; border: 3px solid var(--orange); }
  .front-brand .brand-name { color: var(--front-text); font-size: 40px; letter-spacing: -0.5px; }

  /* Back */
  .card-back {
    left: 560px; top: 470px;
    background: linear-gradient(160deg, var(--card-light-top) 0%, #eeeeee 45%, var(--card-light-bottom) 100%);
  }
  .band-brand {
    position: absolute; left: 0; top: 160px; width: 332px; height: 66px;
    background: var(--band-dark);
    display: flex; align-items: center; gap: 10px; padding-left: 42px;
  }
  .band-brand .brand-dot { width: 30px; height: 30px; border: 3px solid var(--white); }
  .band-brand .brand-name { color: var(--white); font-size: 34px; letter-spacing: -0.5px; }
  .band-name {
    position: absolute; left: 332px; top: 118px; width: 228px; height: 42px;
    background: var(--band-name);
  }
  .person-name {
    position: absolute; left: 360px; top: 94px;
    font-size: 25px; color: var(--name-ink); font-weight: 700;
  }
  .person-role {
    position: absolute; left: 446px; top: 127px;
    font-size: 8px; color: var(--white);
  }
  .accent-bar {
    position: absolute; left: 334px; top: 120px; width: 10px; height: 170px;
    background: var(--orange);
    display: flex; flex-direction: column; justify-content: flex-end; align-items: center;
    padding-bottom: 8px; gap: 10px;
  }
  .accent-bar span { font-size: 7px; color: var(--white); line-height: 1; }
  .contact {
    position: absolute; left: 360px; top: 190px;
    list-style: none; font-size: 12.5px; color: var(--contact-ink); line-height: 17px;
  }
</style>
</head>
<body>
  <section class="card card-front" aria-label="Card front">
    <svg class="front-decoration" width="360" height="320" viewBox="0 0 360 320" aria-hidden="true">
      <circle cx="180" cy="140" r="150" fill="none" stroke="var(--ring-faint)" stroke-width="8"/>
      <circle cx="180" cy="140" r="110" fill="var(--mark-faint)"/>
    </svg>
    <div class="front-brand">
      <span class="brand-dot"></span>
      <span class="brand-name">tarvolink</span>
    </div>
  </section>

  <section class="card card-back" aria-label="Card back">
    <div class="band-name"></div>
    <div class="band-brand">
      <span class="brand-dot"></span>
      <span class="brand-name">tarvolink</span>
    </div>
    <p class="person-name">Liam Carter</p>
    <p class="person-role">general manager</p>
    <div class="accent-bar"><span>t</span><span>e</span><span>w</span></div>
    <ul class="contact">
      <li>03 9555 0182</li>
      <li>carter@tarvolink.com</li>
      <li>www.tarvolink.com</li>
    </ul>
  </section>
</body>
</html>
```